Company letter head

Hello,
We are a global logistics company requiring a letterhead design for all our company documentation.
Company Name: Clearly display the full name of your company at the top of the letterhead.
Logo: Include your company logo for brand recognition.
Contact Information: This includes your company's address, phone number, email address, and website URL.
Target Market(s)
Clients/customers
Industry/Entity Type
Logistics
Font styles to use
Sans Serif
Requirements
Must have
- Company name and logo
Nice to have
- borders, header/footers

```html
<!DOCTYPE html>
<html lang="en">
<head>
<meta charset="utf-8">
<title>Northway Freight Lines – Letterhead</title>
<link href="https://fonts.googleapis.com/css2?family=Open+Sans:wght@400;700&display=swap" rel="stylesheet">
<style>
  :root {
    --backdrop: #d6d6d6;
    --paper: #ffffff;
    --brand-red: #d71f26;
    --charcoal: #3a3a3c;
    --ink: #1d1d1f;
    --watermark: #f1f1f1;
  }
  * { margin: 0; padding: 0; box-sizing: border-box; }
  html, body {
    width: 1200px; height: 686px; overflow: hidden;
    background: var(--backdrop);
    font-family: "Open Sans", sans-serif;
  }
  .letterhead {
    position: absolute; left: 365px; top: 11px;
    width: 470px; height: 664px;
    background: var(--paper);
    box-shadow: 0 6px 18px rgba(0,0,0,.18);
    overflow: hidden;
  }
  .brand {
    position: absolute; top: 58px; right: 40px;
    display: flex; align-items: center; gap: 8px;
  }
  .brand-mark {
    width: 14px; height: 14px; border-radius: 50%;
    background: var(--brand-red);
  }
  .brand-name {
    font-weight: 700; font-size: 15px; color: var(--brand-red);
    text-transform: uppercase; letter-spacing: .3px;
  }
  .watermark {
    position: absolute; left: 70px; top: 190px;
    width: 330px; height: 250px;
    display: flex; align-items: center; justify-content: center;
    text-align: center;
    font-weight: 700; font-size: 46px; line-height: 1.1;
    color: var(--watermark); text-transform: uppercase;
  }
  .contact {
    position: absolute; right: 30px; bottom: 70px;
    list-style: none; text-align: right;
    font-size: 10.5px; line-height: 1.35; color: var(--ink);
  }
  .contact li { display: flex; justify-content: flex-end; align-items: flex-start; gap: 6px; }
  .contact .icon { width: 10px; height: 10px; flex: none; margin-top: 2px; }
  .contact .lines { display: block; }
  .footer-bands { position: absolute; left: 0; bottom: 0; width: 470px; height: 60px; }
</style>
</head>
<body>
  <main class="letterhead">
    <header class="brand">
      <span class="brand-mark"></span>
      <span class="brand-name">Northway Freight Lines</span>
    </header>

    <div class="watermark" role="img" aria-label="Faint company name watermark">Northway<br>Freight<br>Lines</div>

    <ul class="contact">
      <li>
        <span class="lines">27 Harbour Lane<br>Ashford, Kent, TN2 4QD</span>
        <svg class="icon" viewBox="0 0 10 10"><path d="M5 0.5a3.3 3.3 0 0 1 3.3 3.3C8.3 6.3 5 9.5 5 9.5S1.7 6.3 1.7 3.8A3.3 3.3 0 0 1 5 .5z" fill="var(--brand-red)"/><circle cx="5" cy="3.8" r="1.2" fill="#fff"/></svg>
      </li>
      <li>
        <span>(555) 204-7316</span>
        <svg class="icon" viewBox="0 0 10 10"><circle cx="5" cy="5" r="5" fill="var(--brand-red)"/><path d="M3.2 2.5l1 1-.6.8c.4.8 1 1.4 1.8 1.8l.8-.6 1 1-.7.9C4.5 7.2 2.8 5.5 2.5 3.2z" fill="#fff"/></svg>
      </li>
      <li>
        <span>www.northwayfreight.com</span>
        <svg class="icon" viewBox="0 0 10 10"><circle cx="5" cy="5" r="5" fill="var(--brand-red)"/><circle cx="5" cy="5" r="3" fill="none" stroke="#fff" stroke-width=".8"/><path d="M2 5h6M5 2v6" stroke="#fff" stroke-width=".7"/></svg>
      </li>
      <li>
        <span>info@northwayfreight.com</span>
        <svg class="icon" viewBox="0 0 10 10"><circle cx="5" cy="5" r="5" fill="var(--brand-red)"/><rect x="2.3" y="3.2" width="5.4" height="3.8" fill="none" stroke="#fff" stroke-width=".8"/><path d="M2.3 3.2L5 5.3l2.7-2.1" fill="none" stroke="#fff" stroke-width=".8"/></svg>
      </li>
    </ul>

    <svg class="footer-bands" viewBox="0 0 470 60" aria-hidden="true">
      <polygon points="0,14 262,14 252,24 0,24" fill="var(--charcoal)"/>
      <polygon points="112,44 240,44 252,32 470,32 470,60 112,60" fill="var(--brand-red)"/>
    </svg>
  </main>
</body>
</html>
```